Pest control

Pest solutions to all residential and commercial sites, the technicians name will be displayed on the back of the card, and a description of his duties: Pest Technician, Termite Inspector,
Termite protection of properties.
The colours will be all white with VARNO and the 1300 482 157 be a blue.
The file with the phone icon is from my web site.
Residential
VARNO PEST SOLUTIONS, 1300 482 157
varno-example.com.au
info@varno-example.com.au

```html
<!DOCTYPE html>
<html lang="en">
<head>
<meta charset="utf-8">
<title>Varno Pest Solutions – Business Card</title>
<link rel="stylesheet" href="https://fonts.googleapis.com/css2?family=Arimo:wght@400;700&family=Open+Sans:wght@700&family=Parisienne&display=swap">
<style>
  :root {
    --page: #ffffff;
    --card: #f3f3f1;
    --card-edge: #c9c9c6;
    --brand-blue: #4767b7;
    --band-blue: #7f92d2;
    --icon-tint: #dfe3ef;
    --ink: #111111;
  }
  * { margin: 0; padding: 0; box-sizing: border-box; }
  html, body {
    width: 969px; height: 1200px; overflow: hidden;
    background: var(--page);
  }
  .sheet { position: relative; width: 969px; height: 1200px; }

  .card {
    position: absolute; left: 17px; width: 935px; height: 566px;
    background:
      repeating-linear-gradient(180deg, rgba(0,0,0,0.018) 0 2px, transparent 2px 6px),
      var(--card);
    border: 1px solid var(--card-edge);
    box-shadow: 2px 3px 8px rgba(0,0,0,0.35);
    overflow: hidden;
    font-family: "Arimo", Arial, sans-serif;
    color: var(--ink);
  }
  .card--front { top: 14px; }
  .card--back { top: 612px; }

  .pattern-strip {
    position: absolute; left: 24px; right: 24px; height: 52px;
    background: var(--icon-tint); border-radius: 8px; opacity: 0.7;
  }
  .pattern-strip--top { top: 24px; }
  .pattern-strip--bottom { top: 490px; }

  .wordmark {
    position: absolute; font-weight: 700; color: var(--brand-blue);
    line-height: 1; letter-spacing: 1px; white-space: nowrap;
  }
  .tagline {
    position: absolute; font-size: 56px; line-height: 1; color: var(--ink); white-space: nowrap;
  }

  .card--front .wordmark { left: 210px; top: 108px; font-size: 160px; }
  .card--front .tagline { left: 206px; top: 272px; }
  .hotline {
    position: absolute; left: 206px; top: 336px;
    font-weight: 700; font-size: 74px; line-height: 1; color: var(--brand-blue);
  }
  .web, .email {
    position: absolute; top: 414px; font-size: 20px; line-height: 1;
  }
  .web { left: 208px; }
  .email { right: 205px; }

  .band {
    position: absolute; left: 0; top: 26px; width: 410px; height: 232px;
    background:
      repeating-linear-gradient(180deg, rgba(255,255,255,0.08) 0 2px, transparent 2px 5px),
      linear-gradient(90deg, var(--band-blue) 0%, var(--band-blue) 45%, rgba(127,146,210,0) 100%);
  }
  .card--back .wordmark { left: 404px; top: 20px; font-size: 140px; }
  .card--back .tagline { left: 400px; top: 164px; font-size: 54px; }
  .sectors {
    position: absolute; left: 402px; top: 228px;
    font-family: "Open Sans", Arial, sans-serif; font-weight: 700;
    font-size: 26px; line-height: 1; color: var(--brand-blue); letter-spacing: 0.5px;
    white-space: nowrap;
  }

  .technician { position: absolute; left: 22px; top: 328px; }
  .technician__name {
    font-family: "Parisienne", cursive; font-size: 50px; line-height: 1; color: var(--ink);
  }
  .technician__roles { list-style: none; margin-top: 6px; font-size: 22px; line-height: 36px; }
  .technician__phone {
    display: flex; align-items: center; gap: 10px; margin-top: 16px; font-size: 28px;
  }
  .technician__phone svg { width: 26px; height: 26px; }

  .pattern-grid {
    position: absolute; left: 600px; top: 336px; width: 320px; height: 222px;
    background: var(--icon-tint); border-radius: 10px; opacity: 0.7;
  }
</style>
</head>
<body>
<main class="sheet">
  <section class="card card--front" aria-label="Card front">
    <div class="pattern-strip pattern-strip--top" role="img" aria-label="Row of faint pest icons"></div>
    <div class="wordmark">VARNO</div>
    <div class="tagline">PEST SOLUTIONS</div>
    <div class="hotline">1300 482 157</div>
    <div class="web">varno-example.com.au</div>
    <div class="email">info@varno-example.com.au</div>
    <div class="pattern-strip pattern-strip--bottom" role="img" aria-label="Row of faint pest icons"></div>
  </section>

  <section class="card card--back" aria-label="Card back">
    <div class="band"></div>
    <div class="wordmark">VARNO</div>
    <div class="tagline">PEST SOLUTIONS</div>
    <div class="sectors">Commercial and Residential</div>

    <div class="technician">
      <div class="technician__name">Daniel Marlow</div>
      <ul class="technician__roles">
        <li>Pest Technician</li>
        <li>Termite Inspections</li>
        <li>Termite Management</li>
      </ul>
      <div class="technician__phone">
        <svg viewBox="0 0 24 24" aria-hidden="true">
          <rect x="2" y="2" width="20" height="20" rx="4" fill="none" stroke="#111" stroke-width="2"/>
          <path d="M8 7l2 0 1 3-1.5 1a7 7 0 0 0 3.5 3.5l1-1.5 3 1 0 2c0 .8-.7 1.2-1.5 1.2A9 9 0 0 1 6.8 8.5C6.8 7.7 7.2 7 8 7z" fill="#111"/>
        </svg>
        <span>0412 736 905</span>
      </div>
    </div>

    <div class="pattern-grid" role="img" aria-label="Grid of faint pest icons"></div>
  </section>
</main>
</body>
</html>
```